M Zyvantics Buisness Cards

I need a technology focused clean business card for my employees. I have attached out logo to include in the mocks. We're a modern tech consulting firm that drives to interface humanity with technology in a truly cohesive fashion.

```html
<!DOCTYPE html>
<html lang="en">
<head>
<meta charset="utf-8">
<title>M Zyvantics Business Cards</title>
<link rel="stylesheet" href="https://fonts.googleapis.com/css2?family=Josefin+Sans:wght@400;600&display=swap">
<style>
  :root {
    --page: #ecebe8;
    --white: #ffffff;
    --brand-blue: #2f6fe0;
    --brand-grey: #6b7075;
    --icon-grey: #b9bcbf;
    --ink: #4f5357;
    --tint-blue: #a9c2ea;
    --tint-grey: #9a9da1;
  }
  * { box-sizing: border-box; margin: 0; padding: 0; }
  html, body { width: 1200px; height: 1200px; overflow: hidden; }
  body {
    background: var(--page);
    font-family: "Josefin Sans", "Century Gothic", sans-serif;
    position: relative;
  }
  .card {
    position: absolute;
    left: 150px;
    width: 900px;
    height: 514px;
    overflow: hidden;
    box-shadow: 0 10px 28px rgba(0,0,0,0.18);
    background: var(--white);
  }
  .card--details { top: 57px; }
  .card--brand { top: 628px; }

  .brand-field {
    background:
      radial-gradient(ellipse 55% 60% at 50% 50%, #ffffff 35%, rgba(255,255,255,0) 100%),
      linear-gradient(100deg, var(--tint-blue) 0%, #f4f6fa 45%, #f2f2f2 60%, var(--tint-grey) 100%);
  }
  .card--brand { display: flex; align-items: center; justify-content: center; }

  .wordmark {
    display: flex;
    align-items: center;
    gap: 22px;
    color: var(--brand-grey);
    font-weight: 600;
    white-space: nowrap;
  }
  .wordmark__dot {
    border-radius: 50%;
    background: var(--brand-blue);
    flex: none;
  }
  .wordmark--large { font-size: 84px; }
  .wordmark--large .wordmark__dot { width: 46px; height: 46px; }
  .wordmark--small { font-size: 34px; gap: 10px; }
  .wordmark--small .wordmark__dot { width: 20px; height: 20px; }

  .details__brand {
    position: absolute;
    left: 0; top: 0;
    width: 330px; height: 100%;
    display: flex; align-items: center; justify-content: center;
    background:
      radial-gradient(ellipse 70% 55% at 50% 55%, #ffffff 30%, rgba(255,255,255,0) 100%),
      linear-gradient(170deg, var(--tint-blue) 0%, #f3f5f8 45%, var(--tint-grey) 100%);
  }
  .details__band {
    position: absolute;
    left: 330px; top: 0;
    width: 54px; height: 100%;
    background: var(--brand-blue);
  }
  .details__icon {
    position: absolute;
    left: 0;
    width: 54px; height: 54px;
    background: var(--icon-grey);
    display: flex; align-items: center; justify-content: center;
  }
  .details__icon svg { width: 30px; height: 30px; fill: var(--white); }
  .details__lines { position: absolute; left: 0; top: 0; }

  .details__field {
    position: absolute;
    left: 440px; width: 400px;
    text-align: center;
    color: var(--ink);
    font-variant: small-caps;
    letter-spacing: 0.5px;
    font-size: 28px;
  }
  .details__name {
    color: var(--brand-blue);
    font-weight: 600;
    font-size: 36px;
    letter-spacing: 6px;
    font-variant: normal;
    line-height: 1;
  }
  .details__role { font-size: 26px; line-height: 1.1; }
</style>
</head>
<body>

<section class="card card--details" aria-label="Business card, contact side">
  <div class="details__brand">
    <div class="wordmark wordmark--small">
      <span class="wordmark__dot"></span><span>M Zyvantics</span>
    </div>
  </div>

  <div class="details__band">
    <div class="details__icon" style="top:108px">
      <svg viewBox="0 0 24 24"><circle cx="12" cy="7" r="4.5"/><path d="M3 22c0-5 4-8 9-8s9 3 9 8z"/></svg>
    </div>
    <div class="details__icon" style="top:198px">
      <svg viewBox="0 0 24 24"><path d="M6.6 10.8a15 15 0 0 0 6.6 6.6l2.2-2.2c.3-.3.7-.4 1-.2 1.1.4 2.3.6 3.6.6.6 0 1 .4 1 1V20c0 .6-.4 1-1 1A17 17 0 0 1 3 4c0-.6.4-1 1-1h3.5c.6 0 1 .4 1 1 0 1.3.2 2.5.6 3.6.1.3 0 .7-.2 1z"/></svg>
    </div>
    <div class="details__icon" style="top:288px">
      <svg viewBox="0 0 24 24"><text x="12" y="19" text-anchor="middle" font-size="21" font-family="Arial, sans-serif" fill="#fff">@</text></svg>
    </div>
    <div class="details__icon" style="top:378px">
      <svg viewBox="0 0 24 24"><path d="M12 2a7 7 0 0 0-7 7c0 5 7 13 7 13s7-8 7-13a7 7 0 0 0-7-7zm0 9.5A2.5 2.5 0 1 1 12 6.5a2.5 2.5 0 0 1 0 5z"/></svg>
    </div>
  </div>

  <svg class="details__lines" width="900" height="514" viewBox="0 0 900 514" aria-hidden="true">
    <g fill="none" stroke="#2f6fe0" stroke-width="2">
      <path d="M384 168 L424 140 L900 140"/>
      <path d="M384 258 L424 230 L900 230"/>
      <path d="M384 348 L424 320 L900 320"/>
      <path d="M384 438 L424 410 L900 410"/>
    </g>
    <g fill="#5a5e62">
      <circle cx="560" cy="140" r="4.5"/>
      <circle cx="760" cy="140" r="4.5"/>
      <circle cx="500" cy="230" r="4.5"/>
      <circle cx="700" cy="230" r="4.5"/>
      <circle cx="620" cy="320" r="4.5"/>
      <circle cx="820" cy="320" r="4.5"/>
      <circle cx="560" cy="410" r="4.5"/>
      <circle cx="860" cy="410" r="4.5"/>
    </g>
  </svg>

  <div class="details__field" style="top:66px">
    <div class="details__name">YOUR NAME</div>
    <div class="details__role">Your Job</div>
  </div>
  <div class="details__field" style="top:196px">Phone Number</div>
  <div class="details__field" style="top:286px">Email &amp; Website</div>
  <div class="details__field" style="top:376px">Email &amp; Website</div>
</section>

<section class="card card--brand brand-field" aria-label="Business card, brand side">
  <div class="wordmark wordmark--large">
    <span class="wordmark__dot"></span><span>M Zyvantics</span>
  </div>
</section>

</body>
</html>
```